Bright-loop stitchworks Business Card

embroidery printing

Target Market(s)

Businesses and public

Industry/Entity Type

Business

Contact Information for Business Card

Front of card..... Bright-loop stitchworks .... Dorian Felkway..... 868 512-7743.... Email... bright_loopstitchworks@mailvane.net

Back of card..... Bright-loop stitchworks embroidery & artwork

Colors
000000

```html
<!DOCTYPE html>
<html lang="en">
<head>
<meta charset="utf-8">
<title>Bright-loop stitchworks Business Card</title>
<link rel="stylesheet" href="https://fonts.googleapis.com/css2?family=Source+Sans+3:wght@400;600&display=swap">
<style>
  :root {
    --backdrop: #9a9a9a;
    --card-white: #ececec;
    --card-black: #050505;
    --accent-red: #7c1414;
    --text-dark: #1e1e1e;
    --text-grey: #444444;
    --logo-light: #e4e4e4;
    --fine-print: #262626;
    --rule: #3a3a3a;
    --dot-1: #c2463a;
    --dot-2: #3b5998;
    --dot-3: #2a9fd6;
    --dot-4: #1c6fa3;
  }
  html, body {
    margin: 0;
    padding: 0;
    width: 1105px;
    height: 1200px;
    overflow: hidden;
    background: var(--backdrop);
    font-family: "Source Sans 3", "Myriad Pro", Arial, sans-serif;
  }
  .canvas {
    position: relative;
    width: 1105px;
    height: 1200px;
  }
  .card {
    position: absolute;
    left: 182px;
    width: 746px;
    height: 427px;
    overflow: hidden;
  }
  .card-front { top: 119px; background: var(--card-white); }
  .card-back { top: 637px; background: var(--card-black); }

  .corner-art {
    position: absolute;
    inset: 0;
    width: 746px;
    height: 427px;
  }

  .brand-name {
    position: absolute;
    margin: 0;
    font-weight: 600;
    font-size: 34px;
    line-height: 1;
    letter-spacing: 0.5px;
  }
  .card-front .brand-name {
    right: 45px;
    top: 80px;
    color: var(--text-dark);
  }
  .card-back .brand-name {
    left: 0;
    right: 0;
    top: 188px;
    text-align: center;
    font-size: 40px;
    color: var(--logo-light);
  }

  .person {
    position: absolute;
    left: 40px;
    top: 236px;
  }
  .person-name {
    margin: 0;
    font-size: 25px;
    font-weight: 600;
    color: var(--accent-red);
    line-height: 1.2;
  }
  .person-role {
    margin: 2px 0 0;
    font-size: 20px;
    color: var(--text-dark);
    line-height: 1.2;
  }
  .contact-list {
    list-style: none;
    margin: 16px 0 0;
    padding: 0;
  }
  .contact-item {
    display: flex;
    align-items: center;
    gap: 9px;
    height: 28px;
    font-size: 19px;
    color: var(--text-grey);
  }
  .contact-icon { width: 18px; height: 18px; flex: none; }

  .social-row {
    position: absolute;
    left: 0;
    right: 0;
    top: 324px;
    display: flex;
    justify-content: center;
    align-items: center;
    gap: 5px;
  }
  .social-rule {
    width: 66px;
    height: 1px;
    background: var(--rule);
    margin: 0 6px;
  }
  .social-dot {
    width: 32px;
    height: 32px;
    border-radius: 50%;
  }
  .dot-a { background: var(--dot-1); }
  .dot-b { background: var(--dot-2); }
  .dot-c { background: var(--dot-3); }
  .dot-d { background: var(--dot-4); }
  .fine-print {
    position: absolute;
    left: 0;
    right: 0;
    top: 367px;
    margin: 0;
    text-align: center;
    font-size: 13px;
    color: var(--fine-print);
    letter-spacing: 0.5px;
  }
</style>
</head>
<body>
<div class="canvas">

  <section class="card card-front">
    <svg class="corner-art" viewBox="0 0 746 427" aria-hidden="true">
      <path d="M0 0 H170 Q40 60 0 175 Z" fill="var(--card-black)"/>
      <path d="M163 0 Q38 58 4 172" fill="none" stroke="var(--accent-red)" stroke-width="5"/>
      <path d="M746 250 Q700 375 570 427 H746 Z" fill="var(--card-black)"/>
      <path d="M742 258 Q698 372 575 425" fill="none" stroke="var(--accent-red)" stroke-width="5"/>
    </svg>

    <p class="brand-name">Bright-loop stitchworks</p>

    <div class="person">
      <h1 class="person-name">Dorian Felkway</h1>
      <p class="person-role">CEO/Founder</p>
      <ul class="contact-list">
        <li class="contact-item">
          <svg class="contact-icon" viewBox="0 0 18 18" aria-hidden="true">
            <path d="M4 1.5 L7 5 L5.5 7 Q7.5 10.5 11 12.5 L13 11 L16.5 14 L14.5 16.5 Q8 16 3.5 11 Q1 7 1.5 3.5 Z" fill="var(--accent-red)"/>
          </svg>
          <span>868 512-7743</span>
        </li>
        <li class="contact-item">
          <svg class="contact-icon" viewBox="0 0 18 18" aria-hidden="true">
            <rect x="1" y="4" width="16" height="11" fill="var(--accent-red)"/>
            <path d="M1.5 4.5 L9 10 L16.5 4.5" fill="none" stroke="var(--card-white)" stroke-width="1.3"/>
          </svg>
          <span>bright_loopstitchworks@mailvane.net</span>
        </li>
        <li class="contact-item">
          <svg class="contact-icon" viewBox="0 0 18 18" aria-hidden="true">
            <circle cx="9" cy="9" r="8" fill="var(--accent-red)"/>
            <path d="M1 9 H17 M9 1 Q4 9 9 17 M9 1 Q14 9 9 17" fill="none" stroke="var(--card-white)" stroke-width="1.1"/>
          </svg>
          <span>www.brightloopstitch.net</span>
        </li>
      </ul>
    </div>
  </section>

  <section class="card card-back">
    <p class="brand-name">Bright-loop stitchworks</p>
    <div class="social-row" aria-label="Social links">
      <span class="social-rule"></span>
      <span class="social-dot dot-a"></span>
      <span class="social-dot dot-b"></span>
      <span class="social-dot dot-c"></span>
      <span class="social-dot dot-d"></span>
      <span class="social-rule"></span>
    </div>
    <p class="fine-print">Bright-loop stitchworks embroidery &amp; artwork</p>
  </section>

</div>
</body>
</html>
```